Website Re-Design

We would like to explore the possibility of a re-design of our website. We want all the content that it currently has to remain on the pages, and we don't want our logo/corporate identity or colours changed, so it is literally just a website re-design.

Our website is www.trovalink.co.uk

Websites that we like are

http://www.quillmarsh.co.uk/
http://rankwidget.com/

```html
<!DOCTYPE html>
<html lang="en">
<head>
<meta charset="utf-8">
<title>Trovalink – inbound marketing &amp; SEO performance agency</title>
<link rel="stylesheet" href="https://fonts.googleapis.com/css2?family=Source+Sans+3:wght@300;400;600;700&family=Oswald:wght@500&family=Varela+Round&display=swap">
<style>
:root{
  --magenta:#d8127f;
  --green:#8cc63f;
  --teal:#1aa89c;
  --ink:#3a3a3a;
  --body:#4a4a4a;
  --muted:#8a8a8a;
  --band:#ebebeb;
  --footer:#efefef;
  --white:#ffffff;
  --dark:#222222;
}
*{box-sizing:border-box;margin:0;padding:0}
html,body{width:691px;height:1200px;overflow:hidden;background:var(--white)}
body{position:relative;font-family:"Source Sans 3",Arial,sans-serif;color:var(--body)}
.abs{position:absolute}

/* header */
.site-header{position:absolute;left:0;top:0;width:691px;height:61px;background:var(--white)}
.brand{position:absolute;left:73px;top:26px;font-family:"Varela Round",sans-serif;font-size:22px;letter-spacing:0.5px;color:var(--magenta);line-height:1}
.search{position:absolute;left:498px;top:13px;width:119px;height:15px;background:#eeeeee;border:1px solid #e2e2e2;font-size:5px;color:#aaa;padding:4px 6px}
.search svg{position:absolute;right:4px;top:3px}
.main-nav{position:absolute;right:74px;top:36px;display:flex;gap:17px;font-family:"Oswald",sans-serif;font-size:12px;letter-spacing:0.2px;color:#444}
.main-nav .current{color:var(--magenta)}

/* hero */
.hero{position:absolute;left:0;top:61px;width:691px;height:216px;background:var(--band)}
.hero-art{position:absolute;left:0;top:0;width:316px;height:216px;background:linear-gradient(135deg,#f08a2a 0%,#e83b3b 35%,#3aa6e0 65%,#8cc63f 100%)}
.hero-title{position:absolute;left:316px;width:375px;top:70px;text-align:center;font-family:"Varela Round",sans-serif;font-size:37px;color:var(--magenta);line-height:1}
.hero-sub{position:absolute;left:316px;width:375px;top:112px;text-align:center;font-weight:300;font-size:18px;line-height:23px;color:#666}
.dots{position:absolute;left:325px;top:193px;display:flex;gap:2px}
.dots span{width:8px;height:8px;border-radius:50%;background:var(--dark)}
.dots .on{background:#a7c520}

/* intro */
.intro-title{position:absolute;left:0;width:691px;top:287px;text-align:center;font-weight:300;font-size:18px;color:#333}
.intro-title b{font-family:"Varela Round",sans-serif;font-weight:400;font-size:20px;color:var(--magenta)}
.intro-text{position:absolute;left:80px;width:531px;top:320px;text-align:center;font-size:10.5px;line-height:16px;color:#333}

.services{position:absolute;left:70px;top:386px;width:560px;display:flex;justify-content:space-between}
.service{width:180px;text-align:center}
.service h3{font-size:11px;font-weight:600;color:#555;letter-spacing:0.2px}
.service svg{display:block;margin:14px auto 0}
.service p{margin-top:20px;font-size:7px;line-height:14px;color:#444}
.service a{color:var(--magenta);text-decoration:none}
.service.portfolio a{color:var(--green)}
.service.talk a{color:var(--teal)}

/* recent works */
.works{position:absolute;left:0;top:550px;width:691px;height:256px;background:var(--band)}
.section-title{text-align:center;font-size:11px;font-weight:600;color:#555;letter-spacing:0.2px}
.works .section-title{position:absolute;top:18px;width:100%}
.section-text{text-align:center;font-weight:300;font-size:8.5px;line-height:16px;color:var(--muted)}
.works .section-text{position:absolute;left:72px;width:547px;top:39px}
.arrow{position:absolute;top:142px}
.monitor{position:absolute;top:99px;width:145px;height:126px}
.screen{position:absolute;left:6px;top:7px;width:133px;height:76px}

/* clients */
.clients-title{position:absolute;top:827px;width:691px}
.clients-text{position:absolute;left:72px;width:547px;top:849px}
.client-logos{position:absolute;left:110px;top:895px;width:460px;display:flex;justify-content:space-between;align-items:center}
.client{display:flex;align-items:center;gap:5px;font-size:14px;font-weight:600}
.client i{display:block;width:10px;height:10px}
.c1{color:#2a3f8f}.c1 i{background:#2a3f8f;border-radius:50%}
.c2{color:#7a7a7a}.c2 i{background:#5bc2e7}
.c3{color:#d62c2c}.c3 i{background:#d62c2c}
.c4{color:#3f8a3a}.c4 i{background:#e87a22;border-radius:50%}

/* footer */
.site-footer{position:absolute;left:0;top:987px;width:691px;height:213px;background:var(--footer)}
.foot-col{position:absolute;top:18px}
.foot-col h4{font-size:8.5px;font-weight:700;color:#222;letter-spacing:0.2px}
.foot-col ul{list-style:none;margin-top:17px}
.foot-col li,.foot-col p{font-size:7px;line-height:16px;color:#333}
.foot-col p{margin-top:17px}
.foot-col .cta{margin-top:0;font-weight:700;color:#222}
.connect{margin-top:6px;font-size:8px;font-weight:700;color:#222}
.social{display:flex;gap:4px;margin-top:6px}
.social span{width:13px;height:13px;background:var(--dark)}
.copyright{position:absolute;left:0;width:691px;top:1174px;text-align:center;font-size:6.5px;color:#333}
</style>
</head>
<body>

<header class="site-header">
  <div class="brand">TROVALINK</div>
  <div class="search">Type search
    <svg width="8" height="8" viewBox="0 0 8 8"><circle cx="3.2" cy="3.2" r="2.3" fill="none" stroke="#999" stroke-width="1"/><line x1="5" y1="5" x2="7.5" y2="7.5" stroke="#999" stroke-width="1.2"/></svg>
  </div>
  <nav class="main-nav">
    <span class="current">HOME</span><span>ABOUT</span><span>PORTFOLIO</span><span>WHAT WE DO</span><span>CONTACT US</span>
  </nav>
</header>

<section class="hero">
  <div class="hero-art" role="img" aria-label="Cluster of glossy colourful speech-bubble icons for social, search and web services"></div>
  <div class="hero-title">TROVALINK</div>
  <div class="hero-sub">Takes a holistic view of earning<br>your customers attention</div>
  <div class="dots"><span class="on"></span><span></span><span></span><span></span></div>
</section>

<h1 class="intro-title"><b>TROVALINK</b> – your&nbsp; inbound marketing &amp; SEO performance agency</h1>
<p class="intro-text">Do you want to earn your customers attention? Gain more visibility in the SERPs and build &amp; engage with your audience? Trovalink specialises in SEO, Social media, CRO and Design &amp; Creative services. Offering a bespoke and personal service from a team of digital natives.</p>

<section class="services">
  <div class="service">
    <h3>WHAT CAN WE DO FOR YOU?</h3>
    <svg width="64" height="60" viewBox="0 0 64 60">
      <rect x="2" y="2" width="60" height="40" rx="3" fill="var(--magenta)"/>
      <rect x="8" y="8" width="48" height="27" fill="#fff"/>
      <rect x="29" y="42" width="6" height="10" fill="var(--magenta)"/>
      <rect x="20" y="52" width="24" height="4" fill="var(--magenta)"/>
    </svg>
    <p>We offer a bespoke service and will customise to your needs. We specialise in progressive &amp; innovative solutions. <a href="#">Read more &gt;&gt;</a></p>
  </div>
  <div class="service portfolio">
    <h3>SEE OUR PORTFOLIO</h3>
    <svg width="64" height="60" viewBox="0 0 64 60">
      <g transform="rotate(45 32 30)"><rect x="26" y="-4" width="12" height="68" fill="var(--green)"/></g>
      <g transform="rotate(-45 32 30)"><rect x="25" y="0" width="14" height="50" fill="var(--green)"/><polygon points="25,50 39,50 32,62" fill="var(--green)"/></g>
    </svg>
    <p>Take a look at our case-studies to see our recent campaigns showing results achieved for our clients.<br><a href="#">Read more &gt;&gt;</a></p>
  </div>
  <div class="service talk">
    <h3>LET'S TALK</h3>
    <svg width="64" height="60" viewBox="0 0 64 60">
      <rect x="22" y="2" width="20" height="8" rx="2" fill="none" stroke="var(--teal)" stroke-width="4"/>
      <rect x="2" y="10" width="60" height="46" rx="3" fill="var(--teal)"/>
      <line x1="2" y1="30" x2="62" y2="30" stroke="#fff" stroke-width="2"/>
      <rect x="14" y="25" width="8" height="10" fill="var(--teal)" stroke="#fff" stroke-width="2"/>
      <rect x="42" y="25" width="8" height="10" fill="var(--teal)" stroke="#fff" stroke-width="2"/>
    </svg>
    <p>Use our form to send us a message, we will call you back as soon as we can.<br><a href="#">Read more &gt;&gt;</a></p>
  </div>
</section>

<section class="works">
  <h2 class="section-title">RECENT WORKS</h2>
  <p class="section-text">Check out our recent works and case-studies. These are a few examples to show the diversity of work that we can do to earn real attention, generate inbound links, mentions, citations and be used across many of our marketing channels. See more on our portfolio page and learn about what we could do for you.</p>

  <svg class="arrow" style="left:65px" width="13" height="13" viewBox="0 0 13 13"><circle cx="6.5" cy="6.5" r="6.5" fill="#bbb"/><polyline points="8,3.5 5,6.5 8,9.5" fill="none" stroke="#fff" stroke-width="1.6"/></svg>
  <svg class="arrow" style="left:612px" width="13" height="13" viewBox="0 0 13 13"><circle cx="6.5" cy="6.5" r="6.5" fill="#444"/><polyline points="5,3.5 8,6.5 5,9.5" fill="none" stroke="#fff" stroke-width="1.6"/></svg>

  <div class="monitor" style="left:90px">
    <svg width="145" height="126" viewBox="0 0 145 126">
      <rect x="0" y="0" width="145" height="95" rx="3" fill="#1d1d1d"/>
      <rect x="0" y="88" width="145" height="10" fill="#cfcfcf"/>
      <polygon points="58,98 87,98 92,122 53,122" fill="#bdbdbd"/>
      <rect x="48" y="121" width="49" height="4" rx="2" fill="#a9a9a9"/>
    </svg>
    <div class="screen" role="img" aria-label="Video still of a presenter outdoors with a city skyline" style="background:linear-gradient(180deg,#c9d3db,#6e6a5f)"></div>
    <svg class="abs" style="left:50px;top:23px" width="44" height="44" viewBox="0 0 44 44"><circle cx="22" cy="22" r="20" fill="rgba(0,0,0,0.45)" stroke="#fff" stroke-width="2.5"/><polygon points="17,12 32,22 17,32" fill="#fff"/></svg>
  </div>

  <div class="monitor" style="left:274px">
    <svg width="145" height="126" viewBox="0 0 145 126">
      <rect x="0" y="0" width="145" height="95" rx="3" fill="#1d1d1d"/>
      <rect x="0" y="88" width="145" height="10" fill="#cfcfcf"/>
      <polygon points="58,98 87,98 92,122 53,122" fill="#bdbdbd"/>
      <rect x="48" y="121" width="49" height="4" rx="2" fill="#a9a9a9"/>
    </svg>
    <div class="screen" role="img" aria-label="Video still of a studio interview set with bookshelves" style="background:linear-gradient(180deg,#5a2a24,#2a1a1a)"></div>
    <svg class="abs" style="left:50px;top:23px" width="44" height="44" viewBox="0 0 44 44"><circle cx="22" cy="22" r="20" fill="rgba(0,0,0,0.45)" stroke="#fff" stroke-width="2.5"/><polygon points="17,12 32,22 17,32" fill="#fff"/></svg>
  </div>

  <div class="monitor" style="left:456px">
    <svg width="145" height="126" viewBox="0 0 145 126">
      <rect x="0" y="0" width="145" height="95" rx="3" fill="#1d1d1d"/>
      <rect x="0" y="88" width="145" height="10" fill="#cfcfcf"/>
      <polygon points="58,98 87,98 92,122 53,122" fill="#bdbdbd"/>
      <rect x="48" y="121" width="49" height="4" rx="2" fill="#a9a9a9"/>
    </svg>
    <div class="screen" role="img" aria-label="Video still of a pancake in a pan beside travel photos" style="background:linear-gradient(90deg,#e2b15a,#6b7f8f)"></div>
    <svg class="abs" style="left:50px;top:23px" width="44" height="44" viewBox="0 0 44 44"><circle cx="22" cy="22" r="20" fill="rgba(0,0,0,0.45)" stroke="#fff" stroke-width="2.5"/><polygon points="17,12 32,22 17,32" fill="#fff"/></svg>
  </div>
</section>

<h2 class="section-title clients-title">OUR CLIENTS</h2>
<p class="section-text clients-text">We work with and represent a number of progressive companies in their SEO, social, inbound marketing, content and strategy needs. Check out our case-studies for examples.</p>
<div class="client-logos">
  <span class="client c1"><i></i>Tutorwave</span>
  <span class="client c2"><i></i>Wayfarer Guides</span>
  <span class="client c3"><i></i>Staybright</span>
  <span class="client c4"><i></i>Pinecart</span>
</div>

<footer class="site-footer">
  <div class="foot-col" style="left:75px">
    <h4>USEFUL LINKS</h4>
    <ul><li>Home</li><li>About</li><li>Portfolio</li><li>What We Do</li><li>Contact Us</li></ul>
  </div>
  <div class="foot-col" style="left:161px;width:130px">
    <h4>ABOUT US</h4>
    <p>Trovalink is an inbound marketing agency offering a raft of services from digital strategy and planning through to SEO, Social media, SMM, CRO, Design &amp; Creative, through to paid for performance campaigns.</p>
    <p class="cta">Talk to us to discuss your needs.</p>
  </div>
  <div class="foot-col" style="left:305px;width:135px">
    <h4>WHERE ARE WE?</h4>
    <p>We are in London, UK, based down the best mews by the canal, so come check it out and walk the canals with us or we're happy to venture to you!</p>
  </div>
  <div class="foot-col" style="left:443px;width:150px">
    <h4>UK OFFICE</h4>
    <p>7b Alder Wharf, Canal Row, London,<br>UK, W4 2QT<br>Phone: +44 (0) 207 555 0148<br>Email: hello@trovalink.co.uk</p>
    <div class="connect">Connect With Us</div>
    <div class="social" aria-label="Social links"><span></span><span></span><span></span><span></span><span></span></div>
  </div>
</footer>
<p class="copyright">Copyright (c) 2013 Trovalink, All Rights Reserved. Trovalink is the trading name of Trovalink Limited, registered in the UK at Companies House ID:0000000, and VAT registered ID:000 0000 00.</p>

</body>
</html>
```